Women's Health Company needs business card

We need a business card for a USA based women's health care company. We use digital technology to enhance therapy prescribed by clinicians for their patients

```html
<!DOCTYPE html>
<html lang="en">
<head>
<meta charset="utf-8">
<title>Velora Health – Business Card</title>
<link href="https://fonts.googleapis.com/css2?family=Montserrat:wght@400;500&display=swap" rel="stylesheet">
<style>
  :root {
    --bg: #3a3a3a;
    --purple: #a155a3;
    --teal: #35bfbd;
    --white: #ffffff;
  }
  html, body {
    margin: 0;
    padding: 0;
    width: 1200px;
    height: 1200px;
    overflow: hidden;
    background: var(--bg);
    font-family: "Montserrat", Arial, sans-serif;
  }
  .canvas {
    position: relative;
    width: 1200px;
    height: 1200px;
  }
  .card {
    position: absolute;
    left: 250px;
    width: 700px;
    height: 410px;
    border-radius: 28px;
    overflow: hidden;
  }
  .card-front { top: 140px; background: var(--white); }
  .card-back { top: 650px; background: var(--purple); }
  .card-art {
    position: absolute;
    inset: 0;
  }
  .brand {
    position: absolute;
    display: flex;
    align-items: center;
    gap: 14px;
    color: var(--teal);
    font-weight: 500;
    white-space: nowrap;
    line-height: 1;
  }
  .brand-dot {
    width: 14px;
    height: 14px;
    border-radius: 50%;
    background: var(--purple);
  }
  .card-front .brand { left: 66px; top: 78px; font-size: 50px; }
  .card-back .brand { left: 50%; top: 50%; transform: translate(-50%, -50%); font-size: 72px; }
  .card-back .brand-dot { background: var(--white); width: 18px; height: 18px; }
  .holder {
    position: absolute;
    right: 70px;
    top: 240px;
    padding-left: 14px;
    border-left: 4px solid var(--teal);
  }
  .holder-name {
    color: var(--teal);
    font-size: 26px;
    font-weight: 500;
    line-height: 1.1;
  }
  .holder-role {
    color: var(--white);
    font-size: 15px;
    font-weight: 400;
    margin-top: 4px;
  }
  .contacts {
    position: absolute;
    left: 60px;
    bottom: 30px;
    list-style: none;
    margin: 0;
    padding: 0;
    color: var(--white);
    font-size: 17px;
  }
  .contacts li {
    display: flex;
    align-items: center;
    gap: 12px;
    margin-top: 8px;
  }
  .contacts svg { width: 18px; height: 18px; }
</style>
</head>
<body>
<div class="canvas">

  <section class="card card-front">
    <svg class="card-art" viewBox="0 0 700 410" preserveAspectRatio="none" aria-hidden="true">
      <path d="M0,270 Q400,280 700,60 L700,410 L0,410 Z" fill="var(--purple)"/>
      <path d="M0,260 Q400,270 700,48" fill="none" stroke="var(--teal)" stroke-width="7"/>
    </svg>
    <div class="brand"><span class="brand-dot"></span>Velora Health</div>

    <div class="holder">
      <div class="holder-name">JOHN DOE</div>
      <div class="holder-role">CEO | FOUNDER</div>
    </div>

    <ul class="contacts">
      <li>
        <svg viewBox="0 0 24 24"><path fill="var(--teal)" d="M6.6 10.8a15.1 15.1 0 0 0 6.6 6.6l2.2-2.2a1 1 0 0 1 1-.25 11.4 11.4 0 0 0 3.6.57 1 1 0 0 1 1 1V20a1 1 0 0 1-1 1A17 17 0 0 1 3 4a1 1 0 0 1 1-1h3.5a1 1 0 0 1 1 1c0 1.25.2 2.45.57 3.57a1 1 0 0 1-.25 1z"/></svg>
        000 000 0000
      </li>
      <li>
        <svg viewBox="0 0 24 24"><rect x="2" y="5" width="20" height="14" rx="1" fill="var(--teal)"/><path d="M2 6l10 7 10-7" fill="none" stroke="var(--purple)" stroke-width="1.6"/></svg>
        contact@example.com
      </li>
      <li>
        <svg viewBox="0 0 24 24" fill="none" stroke="var(--teal)" stroke-width="1.6"><circle cx="12" cy="12" r="10"/><ellipse cx="12" cy="12" rx="4.5" ry="10"/><path d="M2 12h20M4 7h16M4 17h16"/></svg>
        www.example.com
      </li>
    </ul>
  </section>

  <section class="card card-back">
    <div class="brand"><span class="brand-dot"></span>Velora Health</div>
  </section>

</div>
</body>
</html>
```